Website Design - Photo Shop Design - Functional Cash Register Layout for POS System

Design a webpage for Point of Sale site. A cash register page.

Page must have a good look. I have attached a file of a possible layout example - but need a much nicer design. I have also attached the site logo. which i will upload without background tomorrow hopefully.

Looking for a nice Fresh look , not dark and dingy.

Target Market(s)

Business

Industry/Entity Type

Business Software

Number of Pages Required

1 page

Colors
f59195
f04a50
ec1f27
fbd4d5
ffffff
f8f3f8
fdf0f6
feeeee
ecf5f6

Requirements
Must have
• Cash register layout for POS software site. Nice layout ,
Nice to have
• Try putting he register part on the left side as well as the right - invert the designs have them different to the layout example shown too.
Should not have
• Not to dark

```html
<!DOCTYPE html>
<html lang="en">
<head>
<meta charset="utf-8">
<title>TillNest – Cash Register</title>
<link rel="stylesheet" href="https://fonts.googleapis.com/css2?family=Questrial&family=Montserrat:wght@700&display=swap">
<style>
  :root {
    --red: #ec1f27;
    --red-soft: #f04a50;
    --red-light: #f59195;
    --white: #ffffff;
    --ink: #222222;
    --grey: #666666;
    --rule: #dddddd;
    --label-band: rgba(235, 235, 235, 0.82);
  }
  * { box-sizing: border-box; margin: 0; padding: 0; }
  html, body { width: 1200px; height: 678px; overflow: hidden; background: var(--white); }
  body { font-family: "Questrial", "Century Gothic", sans-serif; color: var(--ink); position: relative; }

  /* ---------- Register panel ---------- */
  .register { position: absolute; left: 0; top: 0; width: 381px; height: 678px; overflow: hidden; background: var(--white); }
  .register-head { position: absolute; left: 0; top: 0; width: 381px; height: 131px; background: var(--red); color: var(--white); }
  .cashier { position: absolute; left: 27px; top: 30px; width: 323px; height: 28px; display: flex; align-items: center; font-size: 17px; }
  .cashier svg { width: 24px; height: 24px; margin-right: 16px; }
  .cashier-name strong { font-family: "Montserrat", sans-serif; font-weight: 700; font-size: 16px; }
  .cashier-time { margin-left: auto; font-size: 17px; letter-spacing: .5px; }
  .head-rule { position: absolute; left: 27px; top: 63px; width: 323px; height: 1px; background: rgba(255,255,255,.55); }
  .transaction { position: absolute; left: 27px; top: 86px; font-size: 17px; }
  .transaction strong { font-family: "Montserrat", sans-serif; font-weight: 700; font-size: 16px; }
  .head-actions { position: absolute; left: 236px; top: 84px; display: flex; gap: 15px; }
  .head-actions svg { width: 26px; height: 26px; }

  .group-title { position: absolute; left: 27px; font-family: "Montserrat", sans-serif; font-weight: 700; font-size: 16px; color: var(--red); }
  .group-rule { position: absolute; left: 27px; width: 323px; height: 1px; background: var(--rule); }

  .line-item { position: absolute; left: 29px; width: 321px; height: 66px; }
  .thumb { position: absolute; left: 0; top: 0; width: 66px; height: 66px; border-radius: 50%;
    background: radial-gradient(circle at 55% 45%, #7a5a3e 0%, #5b3f2a 40%, #8a8f7a 75%, #b7b2a4 100%); }
  .thumb.removing { background: var(--red-soft); display: flex; align-items: center; justify-content: center; }
  .thumb.removing svg { width: 18px; height: 18px; }
  .item-name { position: absolute; left: 77px; top: 18px; font-size: 18px; color: var(--red); white-space: nowrap; }
  .item-size { position: absolute; left: 77px; top: 41px; font-size: 10.5px; color: var(--grey); }
  .item-price { position: absolute; right: 3px; top: 18px; font-size: 18px; color: var(--ink); }
  .item-was { position: absolute; right: 3px; top: 40px; font-size: 10.5px; color: var(--grey); text-decoration: line-through; }

  .payment { position: absolute; left: 0; top: 608px; width: 381px; height: 70px; background: var(--red); color: var(--white);
    display: flex; align-items: center; padding: 0 28px 0 27px; font-size: 18px; }
  .payment svg { width: 14px; height: 14px; margin-left: 12px; }
  .payment-total { margin-left: auto; }

  /* ---------- Catalogue ---------- */
  .topbar { position: absolute; left: 381px; top: 0; width: 819px; height: 131px; background: var(--white); }
  .category-nav { position: absolute; left: 42px; top: 41px; display: flex; align-items: center; height: 45px; }
  .category { font-size: 17px; color: var(--grey); margin-right: 46px; }
  .category.active { color: var(--red); border: 1.5px solid var(--red); padding: 10px 18px; margin-right: 34px; }
  .nav-search { position: absolute; left: 397px; top: 47px; width: 28px; height: 28px; }
  .brand { position: absolute; left: 472px; top: 38px; display: flex; align-items: center; }
  .brand-dot { width: 50px; height: 50px; border-radius: 50%; background: var(--red); margin-right: 12px; }
  .brand-name { font-size: 42px; color: var(--ink); line-height: 1; }
  .brand-sub { position: absolute; left: 1072px; top: 82px; font-size: 9px; color: var(--grey); }

  .product-grid { position: absolute; left: 381px; top: 131px; width: 819px; height: 547px; overflow: hidden; }
  .product { position: absolute; width: 205px; height: 205px; overflow: hidden; }
  .product.wide { width: 190px; }
  .photo { position: absolute; inset: 0; }
  .photo.boots { background: linear-gradient(160deg, #b9b3a1 0%, #7a5a3e 35%, #5a3d28 60%, #8c8470 100%); }
  .photo.watch { background: linear-gradient(100deg, #2a2a2a 0%, #3a3a3a 18%, #e4c3bd 35%, #d8aea8 60%, #eacdc7 80%, #2f2f2f 100%); }
  .product-label { position: absolute; left: 0; bottom: 0; width: 100%; height: 46px; background: var(--label-band);
    display: flex; align-items: center; justify-content: center; font-size: 17px; color: var(--ink); }
  .product.selected .photo { background: linear-gradient(100deg, #d81a22 0%, #ec1f27 40%, #f04a50 100%); }
  .product.selected .product-label { background: transparent; color: var(--white); }
  .qty { position: absolute; left: 0; top: 68px; width: 100%; text-align: center; font-size: 56px; color: var(--white); line-height: 1; }
</style>
</head>
<body>

<aside class="register">
  <header class="register-head">
    <div class="cashier">
      <svg viewBox="0 0 24 24" fill="none" stroke="#fff" stroke-width="2"><circle cx="10" cy="10" r="8"/><circle cx="10" cy="8" r="2.5"/><path d="M5.5 14.5c1.2-2 7.8-2 9 0"/><path d="M16 16l6 6" stroke-linecap="round"/></svg>
      <span class="cashier-name"><strong>Daniel</strong> Ferrow</span>
      <span class="cashier-time">11:15 am</span>
    </div>
    <div class="head-rule"></div>
    <div class="transaction">Transaction #<strong>1535</strong></div>
    <div class="head-actions">
      <svg viewBox="0 0 26 26" fill="none" stroke="#fff" stroke-width="2" stroke-linejoin="round"><path d="M2 14l6 7L24 4"/><path d="M6 14l3 4"/></svg>
      <svg viewBox="0 0 26 26" fill="none" stroke="#fff" stroke-width="3"><circle cx="13" cy="13" r="5"/><path d="M13 2v4M13 20v4M2 13h4M20 13h4M5 5l3 3M18 18l3 3M5 21l3-3M18 8l3-3" stroke-linecap="round"/></svg>
      <svg viewBox="0 0 26 26" fill="none" stroke="#fff" stroke-width="2" stroke-linejoin="round"><path d="M4 22l1.5-5L18 4.5l3.5 3.5L9 20.5z"/><path d="M15.5 7l3.5 3.5"/></svg>
    </div>
  </header>

  <h2 class="group-title" style="top:160px">Boots</h2>
  <div class="group-rule" style="top:189px"></div>

  <div class="line-item" style="top:217px">
    <div class="thumb" role="img" aria-label="Brown leather lace-up boots"></div>
    <span class="item-name">New boots No. 1</span>
    <span class="item-size">Size: 46</span>
    <span class="item-price">$55.30</span>
    <span class="item-was">$89.99</span>
  </div>

  <div class="line-item" style="top:317px">
    <div class="thumb removing" role="img" aria-label="Brown leather boots, marked for removal">
      <svg viewBox="0 0 18 18" stroke="#fff" stroke-width="2.2" stroke-linecap="round"><path d="M2 2l14 14M16 2L2 16"/></svg>
    </div>
    <span class="item-name">New boots No. 1</span>
    <span class="item-size">Size: 46</span>
    <span class="item-price">$55.30</span>
  </div>

  <h2 class="group-title" style="top:419px">Clothes</h2>
  <div class="group-rule" style="top:447px"></div>

  <div class="line-item" style="top:476px">
    <div class="thumb" role="img" aria-label="Brown leather lace-up boots"></div>
    <span class="item-name">New boots No. 1</span>
    <span class="item-size">Size: 46</span>
    <span class="item-price">$55.30</span>
  </div>

  <div class="line-item" style="top:575px">
    <div class="thumb" role="img" aria-label="Brown leather lace-up boots"></div>
    <span class="item-name">New boots No. 1</span>
    <span class="item-size">Size: 46</span>
    <span class="item-price">$55.30</span>
  </div>

  <footer class="payment">
    <span>Payment</span>
    <svg viewBox="0 0 14 14" fill="none" stroke="#fff" stroke-width="1.6" stroke-linejoin="round"><path d="M2 1.5l10 5.5-10 5.5z"/></svg>
    <span class="payment-total">$221.20</span>
  </footer>
</aside>

<header class="topbar">
  <nav class="category-nav">
    <span class="category active">Boots</span>
    <span class="category">Clothes</span>
    <span class="category">Underwear</span>
  </nav>
  <svg class="nav-search" viewBox="0 0 28 28" fill="none" stroke="#555" stroke-width="2.4"><circle cx="11" cy="11" r="8"/><path d="M17 17l8 8" stroke-linecap="round" stroke-width="4"/></svg>
  <div class="brand"><span class="brand-dot"></span><span class="brand-name">TillNest</span></div>
  <span class="brand-sub" style="left:692px">powered by KORA</span>
</header>

<main class="product-grid">
  <div class="product" style="left:0;top:0"><div class="photo boots" role="img" aria-label="Brown leather lace-up boots"></div><span class="product-label">New boots No. 1</span></div>
  <div class="product" style="left:209px;top:0"><div class="photo watch" role="img" aria-label="Wristwatch worn with a leather jacket"></div><span class="product-label">Watch Calder</span></div>
  <div class="product" style="left:418px;top:0"><div class="photo watch" role="img" aria-label="Wristwatch worn with a leather jacket"></div><span class="product-label">Watch Calder</span></div>
  <div class="product wide" style="left:629px;top:0"><div class="photo watch" role="img" aria-label="Wristwatch worn with a leather jacket"></div><span class="product-label">Watch Calder</span></div>

  <div class="product" style="left:0;top:211px"><div class="photo boots" role="img" aria-label="Brown leather lace-up boots"></div><span class="product-label">New boots No. 1</span></div>
  <div class="product selected" style="left:209px;top:211px"><div class="photo" role="img" aria-label="Wristwatch, selected"></div><span class="qty">x1</span><span class="product-label">Watch Calder</span></div>
  <div class="product" style="left:418px;top:211px"><div class="photo watch" role="img" aria-label="Wristwatch worn with a leather jacket"></div><span class="product-label">Watch Calder</span></div>
  <div class="product wide" style="left:629px;top:211px"><div class="photo watch" role="img" aria-label="Wristwatch worn with a leather jacket"></div><span class="product-label">Watch Calder</span></div>

  <div class="product" style="left:0;top:421px"><div class="photo boots" role="img" aria-label="Brown leather lace-up boots"></div></div>
  <div class="product" style="left:209px;top:421px"><div class="photo watch" role="img" aria-label="Wristwatch worn with a leather jacket"></div></div>
  <div class="product" style="left:418px;top:421px"><div class="photo watch" role="img" aria-label="Wristwatch worn with a leather jacket"></div></div>
  <div class="product wide" style="left:629px;top:421px"><div class="photo watch" role="img" aria-label="Wristwatch worn with a leather jacket"></div></div>
</main>

</body>
</html>
```